tamo rix

TAMO RIX mobile technology servicesPhone and tablet repairs, screens data recovery.

Industry/Entity Type

Data Recovery

Contact Information for Business Card

0431 587 612

Colors
33a6d7
f04a50
0a90cc
e34197

Requirements
Must have
• Gary plinth
Nice to have
• White background

```html
<!DOCTYPE html>
<html lang="en">
<head>
<meta charset="utf-8">
<title>TAMO RIX – Business Card</title>
<link rel="stylesheet" href="https://fonts.googleapis.com/css2?family=Roboto+Slab:wght@500;700&display=swap">
<style>
  :root {
    --sky-blue: #33a6d7;
    --deep-blue: #0a90cc;
    --coral-red: #f04a50;
    --card-white: #f7f8f7;
    --backdrop: #e9ecef;
  }
  html, body {
    margin: 0;
    padding: 0;
    width: 1200px;
    height: 800px;
    overflow: hidden;
    background: var(--backdrop);
  }
  .canvas {
    position: relative;
    width: 1200px;
    height: 800px;
    display: flex;
    align-items: center;
    justify-content: center;
  }
  .business-card {
    position: relative;
    width: 360px;
    height: 740px;
    background: var(--card-white);
    box-shadow: 0 2px 10px rgba(0, 0, 0, 0.12);
    font-family: "Roboto Slab", Georgia, serif;
    overflow: hidden;
  }
  .brand-mark {
    position: absolute;
    top: 56px;
    left: 70px;
    width: 260px;
    height: 260px;
  }
  .brand-name {
    position: absolute;
    top: 360px;
    left: 32px;
    margin: 0;
    font-weight: 500;
    font-size: 54px;
    line-height: 1;
    letter-spacing: 1px;
    white-space: nowrap;
    color: var(--deep-blue);
  }
  .person-name {
    position: absolute;
    top: 436px;
    left: 34px;
    margin: 0;
    font-weight: 700;
    font-size: 30px;
    line-height: 1;
    color: var(--coral-red);
  }
  .service-list {
    position: absolute;
    top: 492px;
    left: 34px;
    margin: 0;
    padding: 0;
    list-style: none;
    font-weight: 700;
    font-size: 20px;
    line-height: 30px;
    white-space: nowrap;
    color: var(--sky-blue);
  }
  .contact-phone {
    position: absolute;
    top: 612px;
    left: 34px;
    margin: 0;
    display: flex;
    align-items: center;
    gap: 10px;
    font-weight: 700;
    font-size: 22px;
    line-height: 1;
    color: var(--coral-red);
  }
  .phone-icon {
    width: 22px;
    height: 22px;
    flex: none;
  }
  .accent-bar {
    position: absolute;
    left: 26px;
    right: 70px;
    bottom: 34px;
    height: 8px;
    background: var(--coral-red);
  }
</style>
</head>
<body>
  <main class="canvas">
    <article class="business-card">
      <svg class="brand-mark" viewBox="0 0 260 260" role="img" aria-label="Round blue emblem with a phone repair illustration">
        <circle cx="130" cy="130" r="128" fill="var(--deep-blue)"/>
      </svg>
      <h1 class="brand-name">TAMO RIX</h1>
      <p class="person-name">Gary plinth</p>
      <ul class="service-list">
        <li>Mobile technology services</li>
        <li>Phone and tablet repairs</li>
        <li>Screens data recovery</li>
      </ul>
      <p class="contact-phone">
        <svg class="phone-icon" viewBox="0 0 24 24" aria-hidden="true">
          <path fill="var(--coral-red)" d="M6.6 10.8a15.1 15.1 0 0 0 6.6 6.6l2.2-2.2a1 1 0 0 1 1-.25 11.4 11.4 0 0 0 3.6.57 1 1 0 0 1 1 1V20a1 1 0 0 1-1 1A17 17 0 0 1 3 4a1 1 0 0 1 1-1h3.5a1 1 0 0 1 1 1c0 1.25.2 2.45.57 3.57a1 1 0 0 1-.25 1z"/>
        </svg>
        <span>0431 587 612</span>
      </p>
      <div class="accent-bar"></div>
    </article>
  </main>
</body>
</html>
```